Wordpress and logo Design Project

We need a new very trendy new wordpress design for our mobile app development company www.quillmarkapps.example

We are looking for a new logo design and wordpress theme that looks cool and professional and allows for people visiting the site to see the apps we have developed and also request a quote for us to build their app.

Logo and design need to be fresh and trendy for the mobile space.

Company name is QuillMark Apps www.quillmarkapps.example

Industry/Entity Type

It Company

```html
<!DOCTYPE html>
<html lang="en">
<head>
<meta charset="utf-8">
<title>QuillMark Apps – Mobile Software For Professional Development</title>
<link rel="stylesheet" href="https://fonts.googleapis.com/css2?family=Montserrat:wght@400;700;800&family=Open+Sans:wght@400;600&family=Roboto+Condensed:wght@400;700&family=Playfair+Display:wght@400&display=swap">
<style>
:root{
  --navy:#1f2a3d;
  --ink:#2b2b2b;
  --text:#55595e;
  --muted:#7a7f86;
  --orange-hi:#fff6d8;
  --orange:#ffc247;
  --orange-deep:#f7a21c;
  --accent:#e2412b;
  --accent-2:#c8233f;
  --shelf:#2a2a2c;
  --band-blue:#edf1f6;
  --footer:#f0f0f0;
  --rule:#c9c9c9;
  --link-blue:#3b5998;
}
*{margin:0;padding:0;box-sizing:border-box}
html,body{width:804px;height:1200px;overflow:hidden}
body{position:relative;font-family:"Open Sans",Arial,sans-serif;color:var(--text);background:#fff}
.abs{position:absolute}

/* Hero */
.hero{position:absolute;left:0;top:0;width:804px;height:437px;
  background:radial-gradient(ellipse 520px 360px at 560px 250px,var(--orange-hi) 0%,#ffe7a6 35%,var(--orange) 70%,var(--orange-deep) 100%);}
.hero::after{content:"";position:absolute;left:0;right:0;bottom:0;height:90px;background:linear-gradient(rgba(255,255,255,0),#fff)}
.brand{left:94px;top:24px}
.brand-name{font-family:"Montserrat",sans-serif;font-weight:800;font-size:22px;color:var(--navy);line-height:1}
.brand-tag{font-family:"Montserrat",sans-serif;font-size:9px;color:var(--navy);margin-top:4px}
.search{left:566px;top:14px;width:144px;height:22px;border-radius:11px;background:#fff;box-shadow:0 0 0 3px rgba(255,236,190,.8),inset 0 1px 2px rgba(0,0,0,.2);font-size:8px;color:#777;padding:5px 0 0 22px}
.search svg{position:absolute}
.nav{right:92px;top:46px;display:flex;font-family:"Montserrat",sans-serif;font-weight:700;font-size:9.5px;color:#1b1b1b}
.nav a{color:inherit;text-decoration:none;height:22px;line-height:22px;padding:0 9px}
.nav a.current{background:linear-gradient(#fff4c8,#ffd56a);border-radius:11px;color:var(--accent);padding:0 12px;box-shadow:0 1px 2px rgba(0,0,0,.15)}
.shelf{left:36px;top:345px;width:734px;height:48px}
.device{border-radius:16px;background:linear-gradient(135deg,#3a3d44,#111);}
.headline{left:440px;top:154px;width:280px;text-align:center}
.headline .lead{font-family:"Roboto Condensed",sans-serif;font-size:35px;color:#111;letter-spacing:-1px;line-height:1}
.headline .big{font-family:"Roboto Condensed",sans-serif;font-weight:700;font-size:66px;line-height:1;letter-spacing:-2px;
  background:linear-gradient(90deg,var(--accent-2),var(--accent),#f06a32);-webkit-background-clip:text;background-clip:text;color:transparent;margin-top:4px}
.headline .sub{font-family:"Roboto Condensed",sans-serif;font-weight:700;font-size:11px;letter-spacing:1px;color:#1b1b1b;margin-top:22px}

/* Sections */
.section-title{font-family:"Playfair Display",serif;color:#3a3d42;font-weight:400;line-height:1}
.copy{font-size:9.6px;line-height:14px;color:var(--text)}
.copy p+p{margin-top:14px}
.copy a{color:#111;text-decoration:none}
.who{top:437px;height:215px;background:linear-gradient(#e6eaf0,var(--band-blue) 40%,#f3f5f9);border-top:2px solid #d9dde3}
.mission{top:652px;height:211px;background:linear-gradient(120deg,#dfe4d4 0%,#f1efd9 35%,#f7ecdf 60%,#f5d4d8 100%)}
.idea{top:863px;height:142px;background:#fff}
.band{position:absolute;left:0;width:804px}
.rule{height:2px;background:var(--rule)}

/* Footer */
.footer{top:1005px;height:195px;background:linear-gradient(#e9e9e9,var(--footer) 20%,#fafafa);border-top:3px solid #dcdcdc}
.social{width:137px;height:153px;background:#fff;border:1px solid #b9b9b9}
.social .page{font-size:9px;font-weight:600;color:var(--link-blue)}
.social .like{font-size:7.5px;border:1px solid #9aa6bf;background:#eef1f6;padding:0 3px;color:#333}
.social .count{font-size:7px;color:#333;white-space:nowrap}
.posts h3{font-family:"Playfair Display",serif;font-weight:400;font-size:13px;color:#222}
.posts li{list-style:none;font-size:8px;color:#333;height:19px;line-height:19px;border-bottom:1px solid #e2e2e2;padding-left:8px;position:relative;white-space:nowrap}
.posts li::before{content:"›";position:absolute;left:0;color:#999}
.links{font-size:8px;color:#333;white-space:nowrap}
.links span{color:#999;margin:0 4px}
.legal{font-size:8px;color:#777;line-height:13px;white-space:nowrap}
</style>
</head>
<body>

<header class="hero">
  <div class="abs brand">
    <div class="brand-name">QUILLMARK APPS</div>
    <div class="brand-tag">Mobile Software For Professional Development</div>
  </div>
  <div class="abs search">
    <svg width="8" height="8" style="left:9px;top:7px" viewBox="0 0 8 8"><circle cx="3.3" cy="3.3" r="2.4" fill="none" stroke="#888" stroke-width="1"/><path d="M5 5l2.5 2.5" stroke="#888"/></svg>
    Enter Your Search
    <svg width="12" height="12" style="right:5px;top:5px" viewBox="0 0 12 12"><circle cx="6" cy="6" r="6" fill="#9b9b9b"/><path d="M4 6h4M6.3 4l2 2-2 2" stroke="#fff" stroke-width="1.2" fill="none"/></svg>
  </div>
  <nav class="abs nav">
    <a class="current" href="#">HOME</a><a href="#">POCKETPHONE</a><a href="#">DROIDLINE</a><a href="#">BLOG</a><a href="#">CONTACT</a>
  </nav>

  <svg class="abs shelf" viewBox="0 0 734 48" width="734" height="48">
    <defs><linearGradient id="shelfTop" x1="0" y1="0" x2="0" y2="1"><stop offset="0" stop-color="#4a4a4e"/><stop offset="1" stop-color="#232325"/></linearGradient></defs>
    <ellipse cx="367" cy="44" rx="340" ry="5" fill="rgba(0,0,0,.25)"/>
    <path d="M14 0H720L734 30H0Z" fill="url(#shelfTop)"/>
    <rect x="0" y="30" width="734" height="10" fill="#141415"/>
  </svg>
  <div class="abs device" style="left:110px;top:112px;width:306px;height:238px" role="img" aria-label="Tablet showing a travel photo app with city skyline and stone statue photos"></div>
  <div class="abs device" style="left:338px;top:158px;width:97px;height:204px;border-radius:14px;background:linear-gradient(160deg,#2e3036,#0c0c0e 60%,#4a6a9a)" role="img" aria-label="Phone showing a summer photo collection app"></div>

  <div class="abs headline">
    <div class="lead">Engaging Mobile</div>
    <div class="big">Websites</div>
    <div class="sub">DIFFERENT PLATFORMS, ONE SOLUTIONS</div>
  </div>
</header>

<section class="band who">
  <h2 class="abs section-title" style="left:98px;top:30px;font-size:44px">Who we are</h2>
  <div class="abs copy" style="left:108px;top:86px;width:285px">
    <p>QuillMark is a play on the word “quill mark.” (Who knew that word would be such a popular business name?!)</p>
    <p>Similar to how a quill is a tool used to leave a lasting mark, we hope to use education as a means to induce change in people’s lives. We use mobile software as a medium to help people pursue professional development.</p>
  </div>
  <div class="abs" style="left:483px;top:24px;width:215px;height:191px;border-radius:18px 18px 0 0;background:linear-gradient(135deg,#f4f4f4 0%,#cfcfcf 30%,#1b1b1d 45%,#7a4a22 75%,#b8854c)" role="img" aria-label="Two phones showing a domino game app"></div>
</section>

<section class="band mission">
  <div class="abs" style="left:125px;top:10px;width:127px;height:201px;border-radius:20px 20px 0 0;background:linear-gradient(160deg,#1c1d21,#2b3c4d 45%,#5a3a6a 75%,#1a1a1f)" role="img" aria-label="Phone showing a photo gallery app"></div>
  <h2 class="abs section-title" style="left:316px;top:30px;font-size:44px">Mission</h2>
  <div class="abs copy" style="left:318px;top:86px;width:285px">
    <p>At QuillMark Apps, our mission is to meet our customer’s specific educational needs and provide quality content in an easily digestible format.</p>
    <p>Have an idea for an app that you would like to develop? Reach out and <a href="#">contact us</a></p>
  </div>
</section>

<section class="band idea">
  <div class="abs rule" style="left:96px;top:53px;width:154px"></div>
  <div class="abs rule" style="left:555px;top:53px;width:155px"></div>
  <h2 class="abs section-title" style="left:0;width:804px;text-align:center;top:36px;font-size:34px">Have an app idea?</h2>
  <div class="abs copy" style="left:0;width:800px;text-align:center;top:82px;line-height:14px">
    Have an idea for an app? We would like to hear from you.<br>Reach out and <a href="#">contact us</a>
  </div>
</section>

<footer class="band footer">
  <div class="abs social" style="left:94px;top:19px">
    <div class="abs" style="left:6px;top:6px;width:30px;height:30px;background:#222" role="img" aria-label="Page profile picture"></div>
    <div class="abs page" style="left:41px;top:5px">QuillMark Education</div>
    <div class="abs like" style="left:43px;top:20px">Like</div>
    <div class="abs count" style="left:6px;top:46px">361 people like <span style="color:var(--link-blue)">QuillMark Education</span>.</div>
    <div class="abs" style="left:6px;top:62px;width:100px;height:66px;background:linear-gradient(135deg,#c9a78a,#7b8fa6 50%,#a26a7a)" role="img" aria-label="Grid of follower profile pictures"></div>
    <div class="abs" style="left:5px;top:134px;width:126px;border-top:1px solid #ddd"></div>
    <div class="abs" style="left:6px;top:140px;width:7px;height:7px;background:var(--link-blue)"></div>
    <div class="abs count" style="left:16px;top:138px;font-size:6.5px">Friendbook social plugin</div>
  </div>

  <div class="abs posts" style="left:257px;top:20px;width:235px">
    <h3>Recent Posts</h3>
    <ul style="margin-top:6px">
      <li>MedPrep Review named a top 50 app by Schools.</li>
      <li>PharmTech Exam Review now available on Droidline!</li>
      <li>Interview Coach Pro is here!</li>
      <li>Eight new Education Apps are now available in AppVault</li>
      <li style="border-bottom:none">Career Pathfinder is Released!</li>
    </ul>
  </div>

  <div class="abs links" style="left:512px;top:44px">Home<span>/</span>Contact Us<span>/</span>Pocketphone<span>/</span>Droidline<span>/</span>Blog</div>
  <div class="abs legal" style="left:514px;top:82px">©2013 Copyright by QuillMark Apps.<br>Privacy Policy <span style="margin:0 3px">|</span> Sitemap</div>
</footer>

</body>
</html>
```